Zielgruppe
IT Dienstleistungen, Hardware- u. Softwarevertrieb, Consulting, Sicherheitssysteme
Meine Zielgruppe sind Geschäftskunden (B2B) - Kleine bis mittelständische Unternehmen
Aufgabenstellung
Verschiedene Buttons, wie z.B. Partnernetzwerk, Wir über uns, Aktuelle Angebote, Zertifikate. Die Seite gibt kreativen Spielraum und ist an keinerlei Vorgabe gebunden - Innovatives und modernes Design sind willkommen (darf ruhig mal außergewöhlich sein). Logo ist vorhanden und sollte eingebaut werden (siehe Upload). Anregungen können ebenfalls der Landing Page entnommen werden. Zudem fände ich es gut, wenn einige bewegliche Bilder auf der Seite eingebaut würden und die rote Farbe des Hutes im Layout auftaucht (wenn möglich).

```html
<!DOCTYPE html>
<html lang="en">
<head>
<meta charset="utf-8">
<title>KORVAN-IT – Informationstechnik mit Stil</title>
<link href="https://fonts.googleapis.com/css2?family=Montserrat:wght@500;700;800;900&family=Lato:ital,wght@0,400;0,700;0,900;1,400&display=swap" rel="stylesheet">
<style>
:root{
  --red:#d0262b;
  --red-dark:#a9161c;
  --ink:#3b3b3b;
  --text:#4a4a4a;
  --muted:#7a7a7a;
  --sand:#f3f1ec;
  --panel:#f4f4f5;
  --field:#ebebed;
  --black:#0b0b0b;
  --footer:#333333;
  --white:#ffffff;
}
*{box-sizing:border-box;margin:0;padding:0}
html,body{width:1200px;height:3436px;overflow:hidden}
body{position:relative;background:var(--white);font-family:"Lato",sans-serif;color:var(--text)}
.abs{position:absolute}

/* hero */
.hero{left:0;top:0;width:1200px;height:496px;background:radial-gradient(ellipse at 70% 45%,#2f7fb8 0%,#15426e 35%,#0a1a30 70%,#050a14 100%)}
.hero-art{left:380px;top:60px;width:820px;height:436px;background:radial-gradient(ellipse at 55% 50%,rgba(120,210,240,.45),rgba(40,120,180,.15) 55%,rgba(0,0,0,0) 75%)}
.brand{left:111px;top:36px;display:flex;align-items:center;gap:12px;font-family:"Montserrat",sans-serif;font-weight:800;font-size:26px;color:var(--white);letter-spacing:1px}
.brand-dot{width:22px;height:22px;border-radius:50%;background:var(--red)}
.nav{left:767px;top:62px;display:flex;align-items:center;font-family:"Lato",sans-serif;font-size:14px;color:var(--white);letter-spacing:.5px}
.nav span{margin-right:36px}
.nav .sep{margin-right:36px}
.nav-btn{left:963px;top:56px;width:125px;height:33px;background:var(--red);border-radius:3px;color:var(--white);font-size:13px;display:flex;align-items:center;justify-content:center;letter-spacing:.5px}
.hero-title{left:107px;top:222px;font-family:"Montserrat",sans-serif;font-weight:900;font-size:68px;color:var(--red);letter-spacing:1px;text-shadow:0 3px 8px rgba(0,0,0,.5)}
.hero-sub{left:109px;top:296px;font-size:26px;color:var(--white);letter-spacing:1px}
.band{left:0;top:496px;width:1200px;height:79px;background:var(--black);display:flex;align-items:center;justify-content:center;font-size:24px;color:var(--white);letter-spacing:.5px}
.band em{font-style:normal;color:var(--red)}

/* headings */
.h2{font-family:"Montserrat",sans-serif;font-weight:900;font-size:34px;color:var(--red);letter-spacing:5px}
.center{left:0;width:1200px;text-align:center}

/* about */
.about-h{left:111px;top:651px}
.about-text{left:111px;top:700px;width:480px;font-size:13.3px;line-height:25.7px;color:var(--text)}
.about-text p+p{margin-top:25.7px}
.photo{border-radius:0}
.about-img1{left:612px;top:708px;width:451px;height:163px;background:linear-gradient(90deg,#1d2f45,#5d7590 50%,#c9d3dc)}
.about-img2{left:639px;top:897px;width:449px;height:163px;background:linear-gradient(100deg,#1c1c1c,#8a8a8a 50%,#e4e4e4)}

/* features */
.features{left:0;top:1145px;width:1200px;height:315px;background:var(--sand)}
.feature{top:1218px;width:320px;text-align:center}
.feature svg{display:block;margin:0 auto}
.feature .rule{position:relative;width:104px;height:1px;background:#cfcac0;margin:26px auto 0}
.feature .rule::after{content:"";position:absolute;left:49px;top:-3px;width:6px;height:6px;border-radius:50%;background:var(--red)}
.feature h3{margin-top:22px;font-size:16px;font-weight:700;color:var(--ink);letter-spacing:.3px}
.feature p{margin-top:10px;font-size:13.3px;line-height:21px;color:var(--muted);padding:0 24px}

/* service */
.service-h{top:1535px}
.service-sub{top:1585px;font-size:13.3px;line-height:21px;color:var(--muted)}
.card{top:1665px;width:309px;height:382px;color:var(--white);overflow:hidden}
.card-hw{left:111px;background:linear-gradient(160deg,#0a1c5a,#1d4fd0 40%,#0b1b4a 75%,#050b22)}
.card-sw{left:445px;background:linear-gradient(160deg,#8e1116,#d0262b 45%,#c21f25)}
.card-sf{left:780px;background:linear-gradient(150deg,#1aa6d9,#1675b5 50%,#0c3e6e)}
.card h4{position:absolute;left:25px;font-family:"Montserrat",sans-serif;font-weight:800;font-size:16px;letter-spacing:3px}
.card p{position:absolute;left:25px;width:262px;font-size:13.3px;line-height:20.5px}
.read{position:absolute;left:25px;top:310px;font-size:11.5px;font-weight:900;font-style:italic;letter-spacing:.5px;display:flex;align-items:center;gap:12px}

/* customers */
.customers{left:0;top:2131px;width:1200px;height:438px;background:var(--sand)}
.cust-h{top:2207px}
.avatar{width:142px;height:142px;border-radius:50%;top:2284px}
.av1{left:110px;background:radial-gradient(circle at 50% 40%,#9a8b78,#5a6068 60%,#3b4148)}
.av2{left:613px;background:radial-gradient(circle at 50% 40%,#c7b09a,#6c7280 60%,#e6e8ec)}
.quote{top:2279px;width:318px;font-style:italic;font-size:13.3px;line-height:21px;color:var(--muted)}
.who{top:2376px;font-size:13.3px;font-weight:700;color:var(--ink)}
.who b{color:var(--red);font-weight:700}
.dots{left:0;top:2469px;width:1200px;display:flex;justify-content:center;align-items:center;gap:10px}
.dots i{display:block;border-radius:50%;background:#a8a6a2}

/* certificates */
.cert-h{left:111px;top:2645px}
.cert{width:226px;height:138px;border:1px solid #dcdcdc;background:var(--white);display:flex;align-items:center;justify-content:center}
.badge-blue{width:124px;height:86px;background:#1e9ad8}
.badge-grey{width:122px;height:52px;border-radius:6px;background:linear-gradient(#e9e9e9 50%,#9c9c9c 50%)}
.badge-round{width:90px;height:50px;border-radius:50%;border:4px solid #b01e24}

/* contact */
.contact{left:612px;top:2653px;width:477px;height:531px;background:var(--panel)}
.contact-h{left:612px;top:2706px;width:477px;text-align:center}
.contact-sub{left:612px;top:2754px;width:477px;text-align:center;font-size:13.3px;line-height:21px;color:var(--muted)}
.field{background:var(--field);font-style:italic;font-size:12.5px;color:#9b9b9f;padding:15px 0 0 16px}
.send{left:655px;top:3081px;width:390px;height:42px;background:var(--red);color:var(--white);font-weight:900;font-size:16px;display:flex;align-items:center;justify-content:center}

/* footer */
.footer{left:0;top:3276px;width:1200px;height:160px;background:var(--footer)}
.foot{top:3333px;font-size:13.3px;line-height:25px;color:#e2e2e2;letter-spacing:2px}
</style>
</head>
<body>

<header>
  <div class="abs hero"></div>
  <div class="abs hero-art" role="img" aria-label="Glowing network of connected nodes, mail icons, a tablet and a world map over a globe"></div>
  <div class="abs brand"><span class="brand-dot"></span>KORVAN-IT</div>
  <nav class="abs nav"><span>BEGIN</span><span class="sep">|</span><span>IMPRINT</span></nav>
  <div class="abs nav-btn">CONTACT US</div>
  <h1 class="abs hero-title">KORVAN-IT</h1>
  <div class="abs hero-sub">Informationstechnik mit stil</div>
  <div class="abs band"><span><em>SED</em> UT PERSPICIATIS UNDE <em>(OMNIS ISTE NATUS ERROR)</em> SIT VOLUPTATEM.</span></div>
</header>

<section>
  <h2 class="abs h2 about-h">ABOUT US</h2>
  <div class="abs about-text">
    <p>But I must explain to you how all this mistaken idea of denouncing pleasure and praising pain was born and I will give you a complete account of the system, and expound the actual teachings of the great explorer of the truth, the master-builder of human happiness. No one rejects, dislikes, or avoids pleasure itself, because it is pleasure, but because those who do not know how to pursue pleasure rationally encounter consequences that are extremely painful.</p>
    <p>Nor again is there anyone who loves or pursues or desires to obtain pain of itself, because it is pain, but because occasionally circumstances occur in which toil and pain can procure him some great pleasure. To take a trivial example, which of us ever undertakes laborious physical exercise, except to obtain some advantage from it? But who has any right to find fault with a man who chooses to enjoy a pleasure that has no annoying consequences, or one who avoids a pain that produces no resultant pleasure.</p>
  </div>
  <div class="abs photo about-img1" role="img" aria-label="Two technicians inspecting a server rack in a data centre"></div>
  <div class="abs photo about-img2" role="img" aria-label="Black and white close-up of network cables plugged into a switch"></div>
</section>

<section>
  <div class="abs features"></div>
  <div class="abs feature" style="left:105px">
    <svg width="30" height="34" viewBox="0 0 30 34" fill="none" stroke="#d0262b" stroke-width="1.4"><circle cx="15" cy="8" r="5"/><path d="M5 26v-5a10 8 0 0 1 20 0v5"/><rect x="3" y="25" width="24" height="7"/></svg>
    <div class="rule"></div>
    <h3>INDIVIDUAL IT SOLUTION</h3>
    <p>We plan and implement tailor-made and flexible IT solutions for you.</p>
  </div>
  <div class="abs feature" style="left:440px">
    <svg width="42" height="34" viewBox="0 0 42 34" fill="none" stroke="#d0262b" stroke-width="1.4"><circle cx="13" cy="9" r="4"/><circle cx="29" cy="9" r="4"/><path d="M5 32V20a8 6 0 0 1 16 0v12M21 20a8 6 0 0 1 16 0v12M10 32V24M32 32V24"/><path d="M17 4l4-3 4 3"/></svg>
    <div class="rule"></div>
    <h3>LOCAL PARTNERS</h3>
    <p>As a local partner, we are always at your disposal for you.</p>
  </div>
  <div class="abs feature" style="left:773px">
    <svg width="30" height="36" viewBox="0 0 30 36" fill="none" stroke="#d0262b" stroke-width="1.4"><circle cx="15" cy="13" r="11"/><circle cx="15" cy="13" r="6"/><path d="M8 22l-4 11 5-3 3 4 3-9M22 22l4 11-5-3-3 4-3-9"/></svg>
    <div class="rule"></div>
    <h3>ENGAGED AND QUALIFIED</h3>
    <p>Thanks to our many years of experience, we are able to offer you in-depth know-how.</p>
  </div>
</section>

<section>
  <h2 class="abs h2 center service-h">OUR SERVICE</h2>
  <p class="abs center service-sub">Sed ut perspiciatis unde omnis iste natus error sit voluptatem accusantium doloremque laudantium, totam<br>rem aperiam, eaque ipsa quae ab illo inventore veritatis</p>

  <article class="abs card card-hw" role="img" aria-label="Blue-lit server hardware">
    <h4 style="top:262px">HARDWARE</h4>
    <p style="top:292px">At vero eos et accusamus et iusto odio dignissimos ducimus qui. . .</p>
  </article>
  <article class="abs card card-sw">
    <h4 style="top:60px">SOFTWARE</h4>
    <p style="top:90px">Sed ut perspiciatis unde omnis iste natus error sit voluptatem accusantium doloremque laudantium, totam rem aperiam, eaque ipsa quae ab illo inventore veritatis et quasi architecto beatae vitae dicta sunt explicabo. Nemo enim ipsam voluptatem quia voluptas sit aspernatur aut odit aut fugit, sed quia consequuntur magni dolores eos qui ratione voluptatem sequi nesciunt.</p>
    <div class="read">READ MORE
      <svg width="18" height="10" viewBox="0 0 18 10" fill="none" stroke="#fff" stroke-width="1.4"><path d="M0 5h16M12 1l4 4-4 4"/></svg>
    </div>
  </article>
  <article class="abs card card-sf" role="img" aria-label="Security concept with padlock and network icons">
    <h4 style="top:262px">SAFETY</h4>
    <p style="top:292px">But I must explain to you how all this mistaken idea of denouncing plea. . .</p>
  </article>
</section>

<section>
  <div class="abs customers"></div>
  <h2 class="abs h2 center cust-h">OUR CUSTOMERS</h2>
  <div class="abs avatar av1" role="img" aria-label="Portrait of a customer holding a tablet"></div>
  <p class="abs quote" style="left:267px">"But I must explain to you how all this mistaken idea of denouncing pleasure and praising pain was born and I will give you a complete account"</p>
  <div class="abs who" style="left:269px"><b>HALDERN BROTHERS</b> MARKETING MANAGER</div>
  <div class="abs avatar av2" role="img" aria-label="Portrait of a customer"></div>
  <p class="abs quote" style="left:768px;width:320px">"No one rejects, dislikes, or avoids pleasure itself, because it is pleasure, but because those who do not know how to pursue pleasure rationally encounter consequences that are extremely.</p>
  <div class="abs who" style="left:770px"><b>SELINA</b> DIGITAL MEDIA SPECIALIST</div>
  <div class="abs dots"><i style="width:3px;height:3px"></i><i style="width:6px;height:6px"></i><i style="width:12px;height:12px;background:#d0262b"></i><i style="width:6px;height:6px"></i><i style="width:3px;height:3px"></i></div>
</section>

<section>
  <h2 class="abs h2 cert-h">CERTIFICATES</h2>
  <div class="abs cert" style="left:111px;top:2721px"><div class="badge-round"></div></div>
  <div class="abs cert" style="left:361px;top:2721px"><div class="badge-grey"></div></div>
  <div class="abs cert" style="left:111px;top:2884px"><div class="badge-blue"></div></div>
  <div class="abs cert" style="left:361px;top:2884px"><div class="badge-blue"></div></div>
  <div class="abs cert" style="left:111px;top:3048px"><div class="badge-blue"></div></div>
  <div class="abs cert" style="left:361px;top:3048px"><div class="badge-grey"></div></div>

  <div class="abs contact"></div>
  <h2 class="abs h2 contact-h">CONACT US</h2>
  <p class="abs contact-sub">To take a trivial example, which of us ever undertakes<br>laborious physical exercise,</p>
  <div class="abs field" style="left:655px;top:2836px;width:192px;height:40px">First Name:</div>
  <div class="abs field" style="left:853px;top:2836px;width:192px;height:40px">Last Name:</div>
  <div class="abs field" style="left:655px;top:2887px;width:192px;height:40px">Email:</div>
  <div class="abs field" style="left:853px;top:2887px;width:192px;height:40px">Phone:</div>
  <div class="abs field" style="left:655px;top:2937px;width:390px;height:126px">Message:</div>
  <div class="abs send">SEND</div>
</section>

<footer>
  <div class="abs footer"></div>
  <div class="abs foot" style="left:111px">© 2017 COPYRIGHT KORVAN-IT.<br>ALL RIGHTS RESERVED.</div>
  <div class="abs foot" style="left:869px">EMAIL: INFO@KORVAN-IT.DE<br>TEL: 0 (+49) 2741 / 5530-18</div>
</footer>

</body>
</html>
```